Milk/ Greek yoghurt Packaging design

We need a packaging design for a new dairy processing company based in Kabul called Varnel Dairy. We produce high quality dairy products such as milk, yoghurt, yoghurt drinks. We produce high end Greek yoghurt, milk, salted yoghurt drink called Doogh or Ayran.
The design will be used for three products types.
- Greek yoghurt:50 ml, 250 ml, 400 ml cup packaging
- Ayran(Doogh) 250 ml, 350 ml cup packaing
- Pasteurized milk s 500 ml 1000 ml bottles
Packaging should have the following attritubes
- High end and premium look
- Modern look with lines and fonts
- Information should be both in English and Dari ( we can provide the dari text)
- slogan Premium yoghurt should be mentioned under de logo
We are very inspired by Lustreka yoghurt. Please see the Lustreka packaging for inspiration.
Text for backside of the cup will be provided in two days.
We have two designs for logo. Please see the logo where the cow is on the letter of 'Varnel'. I do not have this logo sperately in good quality.
Regards
محصول از شرکت تولد لبنات ورنل تهیه شده ا با استارتر در چربی ٪3/+ ٪2/
Please mention the sizes of packaging with an error range
± of 10 gram.
Target Market(s)
Kabul,
High end, premium
Industry/Entity Type
It Company
Requirements
Must have
- Modern design, elegant, catchy
Nice to have
- grass

```html
<!DOCTYPE html>
<html lang="en">
<head>
<meta charset="utf-8">
<title>Varnel Dairy – Greek Yoghurt Cup Label</title>
<link href="https://fonts.googleapis.com/css2?family=Questrial&family=Vazirmatn:wght@400&display=swap" rel="stylesheet">
<style>
  :root {
    --backdrop: #e9ebee;
    --label-white: #ffffff;
    --label-edge: #dfe2e6;
    --brand-blue: #1f6fae;
    --brand-blue-light: #3b8fc9;
    --band-yellow: #f5d23a;
    --cream-light: #f7f7f6;
    --cream-shade: #d6d7d8;
    --muted-text: #5b7f9e;
  }
  html, body {
    margin: 0;
    padding: 0;
    width: 1200px;
    height: 1200px;
    overflow: hidden;
    background: var(--backdrop);
    font-family: "Questrial", sans-serif;
  }
  .canvas {
    position: relative;
    width: 1200px;
    height: 1200px;
  }
  .cup-label {
    position: absolute;
    left: 250px;
    top: 170px;
    width: 700px;
    height: 860px;
    background: var(--label-white);
    border: 1px solid var(--label-edge);
    border-radius: 18px;
    box-sizing: border-box;
  }
  .brand {
    position: absolute;
    top: 80px;
    left: 0;
    right: 0;
    display: flex;
    justify-content: center;
    align-items: center;
    gap: 14px;
  }
  .brand-dot {
    width: 22px;
    height: 22px;
    border-radius: 50%;
    background: var(--brand-blue);
  }
  .brand-name {
    font-size: 64px;
    color: var(--brand-blue);
    letter-spacing: 1px;
    line-height: 1;
  }
  .slogan {
    position: absolute;
    top: 168px;
    left: 0;
    right: 0;
    margin: 0;
    text-align: center;
    font-size: 22px;
    letter-spacing: 6px;
    text-transform: uppercase;
    color: var(--muted-text);
    line-height: 1;
  }
  .accent-band {
    position: absolute;
    top: 232px;
    left: 0;
    right: 0;
    height: 26px;
    background: var(--band-yellow);
  }
  .product-name {
    position: absolute;
    top: 285px;
    left: 0;
    right: 0;
    margin: 0;
    text-align: center;
    font-weight: 400;
    font-size: 92px;
    line-height: 1.02;
    color: var(--brand-blue);
    letter-spacing: -1px;
  }
  .product-name .line-two {
    display: block;
    color: var(--brand-blue-light);
  }
  .serving-visual {
    position: absolute;
    left: 215px;
    top: 505px;
  }
  .dari-line {
    position: absolute;
    top: 700px;
    left: 0;
    right: 0;
    margin: 0;
    text-align: center;
    font-family: "Vazirmatn", sans-serif;
    font-size: 26px;
    color: var(--brand-blue);
    line-height: 1.4;
  }
  .net-weight {
    position: absolute;
    top: 770px;
    left: 0;
    right: 0;
    margin: 0;
    text-align: center;
    font-size: 30px;
    color: var(--brand-blue);
    letter-spacing: 1px;
    line-height: 1;
  }
</style>
</head>
<body>
<div class="canvas">
  <section class="cup-label">
    <div class="brand">
      <span class="brand-dot"></span>
      <span class="brand-name">varnel</span>
    </div>
    <p class="slogan">Premium yoghurt</p>
    <div class="accent-band"></div>
    <h1 class="product-name">GREEK<span class="line-two">YOGHURT</span></h1>
    <svg class="serving-visual" width="270" height="170" viewBox="0 0 270 170" role="img" aria-label="Bowl of creamy Greek yoghurt">
      <defs>
        <radialGradient id="creamFill" cx="45%" cy="35%" r="70%">
          <stop offset="0%" stop-color="#f7f7f6"/>
          <stop offset="100%" stop-color="#d6d7d8"/>
        </radialGradient>
      </defs>
      <ellipse cx="135" cy="85" rx="132" ry="82" fill="url(#creamFill)"/>
    </svg>
    <p class="dari-line" dir="rtl" lang="prs">ماست یونانی ممتاز · شرکت لبنیات ورنل · چربی ۳٪</p>
    <p class="net-weight">400 g ± 10 g</p>
  </section>
</div>
</body>
</html>
```